Polish brewery needs BEER LABEL design for WEDDINGS

We need beer label design for weddings. Our brewery is located on South of Poland and it is called Wytwórnia Orlik [PL]/Factory Falcon [ENG]. We feel strong connection to mountains and we use water from the mountain in our vicinity.
Regarding beer style it is India Pale Ale so beer is bitter and aromatic because of high addition of hops. Label design has to be modern and simple. We would prefer bright and cream colors.
We need to have opportunity to edit data which are on the label so we will need to get appropriate files.
In attached files you can find all details. If any additional information will be required please do not hesitate and contact with me.

Target Market(s)

Weddings

Font styles to use
Sans Serif
Script

Colors
ffffff

Requirements
Must have
• Information listed in documents in attached files
Nice to have
• Some nice graphics
Bright and cream colors.
Should not have
• -

```html
<!DOCTYPE html>
<html lang="pl">
<head>
<meta charset="utf-8">
<title>Wedding IPA Label – Wytwórnia Orlik</title>
<link rel="stylesheet" href="https://fonts.googleapis.com/css2?family=Arimo:wght@400;700&family=Smythe&family=Playball&display=swap">
<style>
:root{
  --ink:#111111;
  --grey-text:#5a5a5a;
  --frame:#9b9b9b;
  --rule:#b4b4b4;
  --brown:#7a5a26;
  --paper:#ffffff;
  --mountain:#a3a3a3;
}
*{margin:0;padding:0;box-sizing:border-box}
html,body{width:1200px;height:544px;overflow:hidden;background:var(--paper)}
.label{position:relative;width:1200px;height:544px;font-family:"Arimo",Arial,sans-serif;color:var(--ink);overflow:hidden}
.abs{position:absolute;white-space:nowrap}
.section-title{font-weight:700;color:var(--ink)}

/* left panel */
.ingredients{left:30px;top:44px}
.ingredients .section-title{font-size:21.5px;line-height:24px}
.ingredients p{font-size:21px;line-height:22px;color:var(--grey-text)}
.rules{display:flex;flex-direction:column;justify-content:space-between}
.rules span{display:block;height:1px;background:var(--rule)}
.rules-left{left:29px;top:153px;width:376px;height:27px}
.fact{left:30px;font-size:17.5px;line-height:21px;color:var(--grey-text)}
.fact .section-title{font-size:17.5px}
.fact.sub{font-weight:700}
.fact.volume{color:var(--ink)}
.maker{left:30px;top:427px;font-size:15.5px;line-height:19.5px;color:var(--grey-text);font-style:normal}
.maker .section-title{font-size:16px}
.maker-mark{left:300px;top:422px;width:86px;text-align:center;color:var(--brown);font-size:15px;line-height:18px;white-space:normal}
.maker-mark i{display:block;width:26px;height:42px;margin:0 auto 8px;background:var(--brown)}

/* centre panel */
.frame-outer{left:405px;top:23px;width:390px;height:499px;border:1px solid var(--frame)}
.frame-inner{left:413px;top:31px;width:374px;height:483px;border:4px solid var(--frame);border-radius:26px}
.mountains{left:417px;top:390px;width:366px;height:120px;border-radius:0 0 22px 22px;
  background:linear-gradient(180deg,rgba(163,163,163,0) 0%,var(--mountain) 40%,#cfcfcf 100%)}
.couple{font-family:"Smythe",serif;color:var(--ink);font-size:84px;line-height:84px}
.name-one{left:413px;top:44px;width:374px;text-align:center}
.name-two{left:540px;top:116px;max-width:243px}
.amp{left:475px;top:136px;width:51px;height:51px;border-radius:50%;background:var(--brown);color:var(--paper);
  font-family:"Playball",cursive;font-size:34px;line-height:51px;text-align:center}
.rules-mid{top:233px;height:26px;width:100px}
.rules-mid.l{left:416px}.rules-mid.r{left:684px}
.occasion{left:520px;top:226px;width:160px;text-align:center;font-family:"Smythe",serif;font-size:36px;line-height:40px}
.style-name{left:413px;top:452px;width:374px;text-align:center;font-family:"Playball",cursive;font-size:38px;line-height:50px;color:var(--ink)}

/* right panel */
.description{left:813px;top:33px}
.description .section-title{font-size:21px;line-height:24px}
.description p{font-size:19.5px;line-height:20.8px;color:var(--grey-text)}
.specs{left:820px;top:252px;display:flex;gap:6.5px}
.spec{width:60px;height:60px;border:3px solid var(--ink);display:flex;flex-direction:column;align-items:center;justify-content:center;
  font-size:12.5px;font-weight:700;line-height:18px;text-align:center}
.spec svg{display:block;margin-top:2px}
.rules-right{left:820px;top:377px;width:380px;height:25px}
.social{left:823px;top:422px;font-size:20px;line-height:30px;color:var(--ink)}
.social li{list-style:none;display:flex;align-items:center;gap:6px}
.social li i{display:block;width:21px;height:21px;border-radius:50%;background:var(--ink)}
</style>
</head>
<body>
<div class="label">

  <!-- left panel -->
  <section class="abs ingredients">
    <h2 class="section-title">INGREDIENTS</h2>
    <p>Lista skladników: woda, slód<br>jeczmienny, chmiel, liscie limonki,<br>drozdze.</p>
  </section>
  <div class="abs rules rules-left"><span></span><span></span><span></span><span></span><span></span><span></span></div>

  <div class="abs fact" style="top:204px"><span class="section-title">BEST BEFORE DATE:</span></div>
  <div class="abs fact sub" style="top:226px">Najlepiej spozyc przed:</div>
  <div class="abs fact" style="top:247px">Data stanowi numer partii</div>
  <div class="abs fact" style="top:269px">*leave white blank space for it</div>
  <div class="abs fact volume" style="top:298px"><span class="section-title">VOLUME OF THE BOTTLE:</span> 330ml</div>
  <div class="abs fact" style="top:327px"><span class="section-title">STORAGE CONDITIONS:</span></div>
  <div class="abs fact" style="top:349px">Przechowywac w suchym i ciemnym miejscu</div>
  <div class="abs fact" style="top:371px">*info should appear just under BBD</div>

  <address class="abs maker">
    <div class="section-title">Wytwórnia Orlik</div>
    <div>34-100 Stara Wieś</div>
    <div>Browar Klasztorny Dolina</div>
    <div>Dolina 12, 34-600 Dolina</div>
  </address>
  <div class="abs maker-mark"><i></i>WYTWÓRNIA ORLIK</div>

  <!-- centre panel -->
  <div class="abs frame-outer"></div>
  <div class="abs mountains" role="img" aria-label="Mountain range illustration with the Babia Góra peak"></div>
  <div class="abs frame-inner"></div>

  <div class="abs couple name-one">HELENA</div>
  <div class="abs amp">&amp;</div>
  <div class="abs couple name-two">TOMASZ</div>

  <div class="abs rules rules-mid l"><span></span><span></span><span></span><span></span><span></span></div>
  <div class="abs occasion">WEEDING DATE</div>
  <div class="abs rules rules-mid r"><span></span><span></span><span></span><span></span><span></span></div>

  <div class="abs style-name">India Pale Ale</div>

  <!-- right panel -->
  <section class="abs description">
    <h2 class="section-title">BEER DESCRIPTION</h2>
    <p>Trzymasz w reku nasza autorska<br>IPA do produkcji której wykorzystujemy<br>wode wyplywajaca z samego serca<br>Beskidu Wysokiego – Babiej Góry.<br>IPA lubi chmiele i goryczke, ale zeby<br>nie bylo nudno postanowilismy ja<br>wzbogacic limonka.</p>
  </section>

  <div class="abs specs">
    <div class="spec">ALK<br>5.5%</div>
    <div class="spec">IBU<br>Medium</div>
    <div class="spec">EBC<br>Pale</div>
    <div class="spec">EXT<br>14%</div>
    <div class="spec">WATER
      <svg width="20" height="20" viewBox="0 0 20 22" aria-hidden="true"><path d="M10 1 C10 1 3 10 3 14 a7 7 0 0 0 14 0 C17 10 10 1 10 1Z" fill="#111"/></svg>
    </div>
  </div>

  <div class="abs rules rules-right"><span></span><span></span><span></span><span></span><span></span><span></span></div>

  <ul class="abs social">
    <li><i></i>wytworniaorlik</li>
    <li><i></i>orlik.browar</li>
    <li><i></i>www.wytworniaorlik.pl</li>
  </ul>

</div>
</body>
</html>
```